Crestway screen porch

Can you please design a flyer for me promoting my screen porch businessPlease remove the seamless gutters word from the title and add “screen porches” I have added the logo and a bunch of pictures from projects that I have done in the past. You can use words like Hillcrest Screen porches, etc

Target Market(s)

homeowners, contractors, builders

Industry/Entity Type

Construction

Requirements
Must have
• Dom Karsten
• Crestway Gutters
• 2957 Old Hwy 38 N, Briarton, ST 29873
• 555-555-0186
Nice to have
• A few colors maybe 3 most
• nice looking font

```html
<!DOCTYPE html>
<html lang="en">
<head>
<meta charset="utf-8">
<title>Crestway Screen Porches Flyer</title>
<link href="https://fonts.googleapis.com/css2?family=Oswald:wght@400;500;600&display=swap" rel="stylesheet">
<style>
  :root {
    --red: #d4152f;
    --black: #0d0d0d;
    --white: #ffffff;
    --backdrop: #d9d9d9;
    --wood: #8a6a40;
    --siding: #c9c7be;
    --sky: #9db4c9;
    --screen: #3c3f44;
    --lawn: #6d7a4a;
  }
  * { box-sizing: border-box; margin: 0; padding: 0; }
  html, body {
    width: 1200px; height: 1000px; overflow: hidden;
    background: linear-gradient(180deg, #e6e6e6, var(--backdrop));
    font-family: "Oswald", "Arial Narrow", sans-serif;
  }
  .flyer {
    position: absolute; left: 370px; top: 40px;
    width: 460px; height: 920px;
    background: var(--white);
    padding: 0 20px;
    box-shadow: 0 6px 24px rgba(0,0,0,.25);
    display: flex; flex-direction: column;
    overflow: hidden;
  }
  .brand {
    height: 318px;
    display: flex; flex-direction: column; align-items: center; justify-content: center;
    color: var(--red); font-weight: 600; text-transform: uppercase; line-height: 1;
  }
  .brand-name { font-size: 100px; letter-spacing: 2px; }
  .brand-tag { font-size: 42px; letter-spacing: 3px; margin-top: 10px; }
  .hero {
    height: 228px; display: flex;
    border-top: 4px solid var(--red); border-bottom: 4px solid var(--red);
  }
  .hero-title {
    width: 56%; background: var(--red); color: var(--white);
    font-weight: 500; font-size: 46px; line-height: 1.05; text-transform: uppercase;
    padding: 16px 14px; display: flex; flex-direction: column; justify-content: center;
    white-space: nowrap; overflow: hidden;
  }
  .hero-photo {
    flex: 1;
    background: linear-gradient(160deg, var(--sky) 0%, #6f7d6a 40%, var(--wood) 75%, #4a3a28 100%);
  }
  .photo-row { display: flex; gap: 4px; }
  .photo-row.top { height: 124px; padding-top: 4px; }
  .photo-row.bottom { height: 107px; }
  .photo { flex: 1; }
  .p1 { background: linear-gradient(180deg, #b8c4cf, var(--screen) 55%, var(--wood)); }
  .p2 { background: linear-gradient(180deg, #a9b7c4, #e8e8e4 45%, var(--screen) 80%); }
  .p3 { background: linear-gradient(180deg, #aebdca, var(--siding) 40%, #f1f1ee 85%); }
  .p4 { background: linear-gradient(180deg, #d8d6ca, var(--siding) 50%, var(--lawn)); }
  .p5 { background: linear-gradient(180deg, #8fa6c4, #6a6aa0 40%, #c7b9a2 85%); }
  .p6 { background: linear-gradient(180deg, #b6c3d0, var(--screen) 45%, var(--lawn)); }
  .contact {
    height: 141px; background: var(--black); color: var(--white);
    display: flex; flex-direction: column; align-items: center; justify-content: center;
    gap: 8px; margin: 4px 0;
  }
  .contact-names { font-size: 28px; font-weight: 500; }
  .contact-address { font-size: 21px; font-weight: 400; }
  .contact-phone { font-size: 23px; font-weight: 400; display: flex; align-items: center; gap: 8px; }
  .contact-phone svg { width: 20px; height: 20px; }
</style>
</head>
<body>
  <main class="flyer">
    <header class="brand">
      <span class="brand-name">Crestway</span>
      <span class="brand-tag">Screen Porches</span>
    </header>

    <section class="hero">
      <h1 class="hero-title">
        <span>Hillcrest</span><span>Screen</span><span>Porches</span>
      </h1>
      <div class="hero-photo" role="img" aria-label="Photo of a finished screened porch with black railing and wooded yard view"></div>
    </section>

    <section class="photo-row top">
      <div class="photo p1" role="img" aria-label="Photo of a raised screened porch with gable roof"></div>
      <div class="photo p2" role="img" aria-label="Photo of a white-trimmed screened porch addition"></div>
      <div class="photo p3" role="img" aria-label="Photo of a screened porch with stairs on a two-story home"></div>
    </section>

    <section class="contact">
      <p class="contact-names">Dom Karsten • Crestway Gutters</p>
      <p class="contact-address">2957 Old Hwy 38 N, Briarton, ST 29873</p>
      <p class="contact-phone">
        <svg viewBox="0 0 20 20" aria-hidden="true">
          <circle cx="10" cy="10" r="8.5" fill="none" stroke="#fff" stroke-width="1.6"/>
          <path d="M7 5.5c-1 .8-1.3 2-.7 3.5 1 2.3 2.5 3.8 4.7 4.8 1.3.5 2.4.2 3.2-.8l-1.8-1.6-1.2.8c-1.2-.6-2-1.4-2.6-2.6l.8-1.2z" fill="#fff"/>
        </svg>
        555-555-0186
      </p>
    </section>

    <section class="photo-row bottom">
      <div class="photo p4" role="img" aria-label="Photo of a screened porch on a beige-sided house"></div>
      <div class="photo p5" role="img" aria-label="Photo of a two-level screened porch on a blue house"></div>
      <div class="photo p6" role="img" aria-label="Photo of a dark-screened porch above a green lawn"></div>
    </section>
  </main>
</body>
</html>
```